Large Financial Advisory Firm Needs a Brochure!

We are looking for a modern and professional 4 page brochure for our Financial Advisory firm, Harbrook Counsel Group. I've attached multiple files to help with the completion of the design.
SIZE OF BROCHURE: 17 x 11 FLAT, 8.5 x 11 inch FOLDED
1. A PDF titled Design Brief will provide you with an overview of the project, the text to be included in the brochure and other misc. instructions.
2. Logo Files, you will need to incorporate our logo into the brochure design, I've attached all the files please select the images that suit your design.
3. Competitor Illustration - I've attached an image that needs to be included on the 2nd page (inside left cover of the brochure). You will need to incorporate the pros/cons of using our competitors and the advantages of using our firm. This is outlined in the Design Brief PDF.
NOTE: If possible please get rid of the blue sky in the illustration. Just use the buildings, the blue throws off the concept. I contacted the illustrator and am waiting for a design without the sky but it may not be ready in time so please delete it if possible.
- I like the Avenir fonts, 85 Heavy, 65 Medium and 45.

```html
<!DOCTYPE html>
<html lang="en">
<head>
<meta charset="utf-8">
<title>Harbrook Counsel Group – Brochure Cover</title>
<link href="https://fonts.googleapis.com/css2?family=Bebas+Neue&family=Mulish:wght@500&display=swap" rel="stylesheet">
<style>
  :root {
    --gold-deep: #e6ab24;
    --gold-mid: #ecb52e;
    --gold-light: #f3c140;
    --gold-pale: #f5c85a;
    --paper: #ffffff;
    --tagline-shadow: rgba(120, 70, 0, 0.35);
  }
  * { margin: 0; padding: 0; box-sizing: border-box; }
  html, body {
    width: 1000px;
    height: 1200px;
    overflow: hidden;
    background: var(--gold-mid);
  }
  .cover {
    position: relative;
    width: 1000px;
    height: 1200px;
    overflow: hidden;
    background: linear-gradient(160deg, var(--gold-deep) 0%, var(--gold-mid) 45%, var(--gold-light) 100%);
  }
  .cover-wave {
    position: absolute;
    inset: 0;
    width: 1000px;
    height: 1200px;
  }
  .brand {
    position: absolute;
    top: 88px;
    left: 0;
    width: 1000px;
    text-align: center;
    color: var(--paper);
    font-family: "Mulish", "Avenir", sans-serif;
    font-weight: 500;
  }
  .brand-square {
    display: block;
    width: 150px;
    height: 150px;
    margin: 0 auto;
    border: 10px solid var(--paper);
  }
  .brand-name {
    margin-top: 72px;
    font-size: 96px;
    line-height: 1;
    letter-spacing: 0.04em;
    text-transform: uppercase;
  }
  .brand-sub {
    display: block;
    margin-top: 22px;
    font-size: 44px;
    letter-spacing: 0.32em;
    margin-right: -0.32em;
  }
  .tagline {
    position: absolute;
    right: 50px;
    top: 632px;
    text-align: right;
    color: var(--paper);
    font-family: "Bebas Neue", "Oswald", sans-serif;
    font-size: 118px;
    line-height: 116px;
    letter-spacing: 0.01em;
    text-shadow: 3px 4px 6px var(--tagline-shadow);
  }
</style>
</head>
<body>
<main class="cover">
  <svg class="cover-wave" viewBox="0 0 1000 1200" aria-hidden="true">
    <defs>
      <linearGradient id="lowerTone" x1="0" y1="0" x2="1" y2="1">
        <stop offset="0" stop-color="#f0b522"/>
        <stop offset="1" stop-color="#f5c85a"/>
      </linearGradient>
    </defs>
    <path class="lower-field" d="M0,580 C120,560 220,640 330,790 C430,930 520,1060 700,1090 C820,1105 920,1080 1000,1050 L1000,1200 L0,1200 Z" fill="url(#lowerTone)"/>
    <path class="wave-band" d="M0,580 C120,560 220,640 330,790 C430,930 520,1060 700,1090 C820,1105 920,1080 1000,1050" fill="none" stroke="#ffffff" stroke-width="28"/>
  </svg>

  <header class="brand">
    <span class="brand-square"></span>
    <h1 class="brand-name">Harbrook<span class="brand-sub">Counsel Group</span></h1>
  </header>

  <h2 class="tagline">Redefining<br>Investment<br>Advice</h2>
</main>
</body>
</html>
```